VELT needs a simple, contemporary and easy to use 'designer' website (fully working/coded)

VELT is a progressive market research consultancy based in Sydney, Australia. We are a new company and require a contemporary/modern and bold, uncomplicated/simple, clean/uncluttered site, which uses friendly and easy to read fonts. The brand is approachable. The colour palate should be simple and contemporary. Colours used in our logo are:#FFCC00 and #404041 so any others should complement these.

The following website gives a really good idea of how simple the site should be: www.brightmarrow.com.au and I am looking to create something similar to this style of site (but not necessarily copied).

The website should convey ‘different types of customer’. VELT helps different companies ‘connect’ with their particular shoppers or end users of their product. This could be a mum doing the washing, a dad cleaning the car, children eating ice cream, old people reading the newspaper, someone trying on glasses, someone buying petfood etc. Alternatively it could simply just be pictures of different people…different ages, different nationalities, different employment types etc, but they should give a positive impression (ie people smiling/laughing) and also GREAT quality photos.

Content will also be attached but please note this is just a draft reference and will be sent to a copywriter for improvement. The telephone number is yet to be confirmed but will be given at the end of the contest.

The navigation may borrow strongly from www.brightmarrow.com.au. It may have the following navigation panel:

ABOUT US

WHAT WE DO

> NPD

> PRODUCT TESTING

> SHOPPER

> SEGMENTATION

> ONLINE COMMUNITIES

> CUSTOMER EXPERIENCE

> VISUALISATION

> TAILOR MADE

CONTACT US

The home page may be WHAT WE DO and each picture represents one of the 8 sections (such as NPD) etc.

One of my main objectives is also to get people to sign up to my quarterly newsletter, so would like to make this very visible, and make it easy for them to connect via workmesh.

I will also want to add a blog page in September (so needs to be hidden now but switched on in Sept). This blog will contain articles from the newsletters and workmesh updates. I may also want to add a simple 90-180 second video at the bottom of each of the 8 sections (to be added over the next 12 months but i would like to ensure it is possible to do this at a later stage).

The logo has recently been designed and i have attcahed different colour versions as i may be swayed depending on hoe they look in te website. I tend to prefer yellow on white, or white on yellow but other optins are included if you think they work better with your design.

Target Market(s)

Professionals in large blue chip companies..such as pino fizz, varona, tamborix etc. Marketing Managers/Directors, PR and advertising agencies etc.

Industry/Entity Type

Progressive

Requirements
Must have
• High quality positive photos. Be very easy to navigate...should scream simple!

```html
<!DOCTYPE html>
<html lang="en">
<head>
<meta charset="utf-8">
<title>VELT — progressive research</title>
<link href="https://fonts.googleapis.com/css2?family=Barlow:ital,wght@0,400;0,500;0,700;1,600&display=swap" rel="stylesheet">
<style>
:root{
  --yellow:#FFCC00;
  --charcoal:#404041;
  --ink:#3a3a3b;
  --white:#ffffff;
  --photo-a:#6e6e6e;
  --photo-b:#b9b9b9;
}
*{margin:0;padding:0;box-sizing:border-box}
html,body{width:1200px;height:2471px;overflow:hidden}
body{position:relative;background:var(--white);font-family:"Barlow",Arial,sans-serif;color:var(--ink)}
.abs{position:absolute}
.brand{font-weight:700;font-size:38px;letter-spacing:2px;color:var(--charcoal);line-height:1}
.brand--small{font-size:18px;letter-spacing:1px}
.center{left:0;width:1200px;display:flex;justify-content:center}
.subscribe{left:406px;top:379px;width:374px;height:55px;background:var(--yellow);color:var(--charcoal);font-weight:700;font-size:20px;letter-spacing:3px;display:flex;align-items:center;justify-content:center}
.enter{top:446px;font-weight:700;font-size:20px;letter-spacing:3px;color:var(--charcoal)}
.rights{font-weight:700;font-size:14px;letter-spacing:2px;color:var(--charcoal)}
.navbar{left:0;top:879px;width:1200px;height:49px;background:var(--charcoal)}
.navbar .brand{position:absolute;left:365px;top:11px;color:var(--yellow);font-size:28px}
.nav-link{position:absolute;top:16px;color:var(--white);font-weight:700;font-size:15px;letter-spacing:1.5px}
.nav-news{position:absolute;left:876px;top:11px;color:var(--yellow);font-size:22px;font-weight:500;letter-spacing:1px}
.nav-mark{left:876px;top:928px;width:4px;height:10px;background:var(--yellow)}
.photo{position:absolute;left:228px;width:132px;background:linear-gradient(135deg,var(--photo-a),var(--photo-b))}
.feature-panel{left:431px;top:1065px;width:354px;height:135px}
.feature-title{left:452px;top:1080px;color:var(--white);font-weight:700;font-size:20px;letter-spacing:2px}
.feature-copy{left:452px;top:1118px;width:200px;font-size:12px;font-weight:700;line-height:1.4;letter-spacing:.5px;color:var(--charcoal)}
.read-more{left:690px;top:1187px;color:var(--yellow);font-weight:700;font-size:14px;letter-spacing:2px}
.tagline{left:27px;top:1745px;color:var(--yellow);font-style:italic;font-weight:600;font-size:36px;letter-spacing:2px}
.about-title{left:36px;top:1833px;font-weight:700;font-size:34px;color:var(--charcoal)}
.about-copy{left:41px;top:1890px;width:602px;font-size:14.5px;line-height:1.45;color:var(--ink);text-align:justify}
.about-copy p{margin-bottom:18px}
.about-copy p.gap{margin-top:64px}
.offer{left:697px;top:1840px;width:462px;height:538px;background:var(--yellow);padding:14px 16px;color:var(--white)}
.offer h3{font-weight:700;font-size:20px;letter-spacing:.5px;margin-bottom:26px}
.offer h3.second{margin-top:92px}
.offer ul{list-style:none;font-size:14.5px;line-height:1.42}
.offer li{position:relative;padding-left:24px}
.offer li::before{content:"";position:absolute;left:2px;top:5px;width:10px;height:5px;border-left:2px solid var(--white);border-bottom:2px solid var(--white);transform:rotate(-45deg)}
.view-all{left:41px;top:2336px;color:var(--yellow);font-size:34px;font-weight:500;letter-spacing:3px}
</style>
</head>
<body>
<!-- splash -->
<div class="abs center" style="top:54px"><div class="brand">VELT</div></div>
<div class="abs subscribe">SUBSCRIBE OUR NEWSLETTER</div>
<div class="abs center enter">ENTER</div>
<div class="abs center rights" style="top:764px">ALL RIGHTS RESERVED 2013</div>
<div class="abs center" style="top:787px"><div class="brand brand--small">VELT</div></div>

<!-- projects -->
<nav class="abs navbar">
  <div class="brand">VELT</div>
  <span class="nav-link" style="left:486px">ABOUT US</span>
  <span class="nav-link" style="left:601px">WHAT WE DO</span>
  <span class="nav-link" style="left:730px">CONTACT US</span>
  <span class="nav-news">newsletter</span>
</nav>
<div class="abs nav-mark"></div>

<div class="photo" style="top:956px;height:98px" role="img" aria-label="Project photo: smiling shopper"></div>
<div class="photo" style="top:1065px;height:135px" role="img" aria-label="Featured project photo: cheerful older man"></div>
<svg class="abs feature-panel" viewBox="0 0 354 135" aria-hidden="true"><polygon points="0,0 354,0 250,104 0,104" fill="var(--yellow)"/></svg>
<div class="abs feature-title">PROJECT NAME HERE</div>
<div class="abs feature-copy">Lorem ipsum dolor sit amet, consectetur adipiscing elit.</div>
<div class="abs read-more">READ MORE</div>
<div class="photo" style="top:1216px;height:99px" role="img" aria-label="Project photo: parent playing with child"></div>
<div class="photo" style="top:1329px;height:99px" role="img" aria-label="Project photo: young child smiling"></div>
<div class="photo" style="top:1439px;height:99px" role="img" aria-label="Project photo: laughing woman"></div>
<div class="photo" style="top:1549px;height:99px" role="img" aria-label="Project photo: friends together"></div>

<!-- about -->
<div class="abs tagline">“Progressive research”</div>
<h2 class="abs about-title">Who we are.</h2>
<div class="abs about-copy">
  <p>Velt is a progressive technology friendly research agency, specialising in consumer and shopper research. We help companies understand the ever-changing relationships people have with media, services, products and brands by combining innovative methods, creative thinking, research expertise and a deep understanding of shopper and consumer decision-making.</p>
  <p>Velt was established by Dana Morrow who has 15 years global consumer and shopper research experience. Prior to setting up velt, Dana was General Manager of a consumer research agency, and more recently, General Manager of a specialist shopper research agency.</p>
  <p class="gap">We take a smart, human approach to research, and understand that what people say, and what people do, are often very different things. As Harlan Brooke once famously said, ‘If I had asked my customers what they wanted, they would have said a faster horse’! We know how to ask questions, and how to translate the results into actionable recommendations.</p>
  <p>We offer cost effective, multi-faceted research, designed and managed by experienced practitioners, using award winning online, mobile, community and video based research applications.</p>
</div>
<section class="abs offer">
  <h3>At velt we can:</h3>
  <ul>
    <li>gauge how your target market thinks about certain topics, services or products</li>
    <li>help improve current products or services</li>
    <li>understand the likely impact of any proposed changes</li>
    <li>identify new opportunities</li>
    <li>understand strengths and weaknesses versus competitors</li>
  </ul>
  <h3 class="second">We:</h3>
  <ul>
    <li>Have knowledgeable staff</li>
    <li>Listen carefully to truly understand your needs</li>
    <li>Talk plain English</li>
    <li>Are easy to work with</li>
    <li>Aim to ‘wow’ our clients</li>
    <li>Are committed to continued improvement</li>
    <li>Complete projects in agreed timings</li>
    <li>Respond quickly to requests</li>
    <li>Pride ourselves on quality research and actionable outputs</li>
  </ul>
</section>
<div class="abs view-all">view all projects</div>
<div class="abs center rights" style="top:2411px">ALL RIGHTS RESERVED 2013</div>
<div class="abs center" style="top:2434px"><div class="brand brand--small">VELT</div></div>
</body>
</html>
```